Cosmetics Store Website

High end cosmetics/skincare store needs a new website. We are a locally owned company based in Idaho. We have an initial site map and some copy and we are looking for someone who can not only DESIGN but get a full website UP AND RUNNING! This will not be a shopping cart style site (we do not sell online) but rather an information site about our locations, our brands, our services, our mission, job opportunities etc. We would like to see a mock up of our home page and hear how you plan to code/set up the rest of our site. We would prefer to keep the company name confidential, but know that our logo is black and just a stylized lettering of our company name.
More details like company name, logo, pictures, etc can be given after we select a candidate.
Thank you!

```html
<!DOCTYPE html>
<html lang="en">
<head>
<meta charset="utf-8">
<title>Cosmetics Store – Website Screens</title>
<link href="https://fonts.googleapis.com/css2?family=Arimo:wght@400;700&display=swap" rel="stylesheet">
<style>
:root{
  --ink:#000;
  --red:#e3120b;
  --paper-hi:#d2d2d2;
  --paper-lo:#a3a3a3;
  --text-dark:#1a1a1a;
  --text-mid:#3a3a3a;
  --nav-text:#9a9a9a;
  --white:#fff;
  --highlight:#f3df77;
  --strip:#3c3c3c;
  --button:#8e8e8e;
  --divider:#444;
  --rule:#8c8c8c;
}
*{box-sizing:border-box;margin:0;padding:0}
html,body{width:1200px;height:900px;overflow:hidden;background:var(--ink)}
body{position:relative;font-family:"Arimo",Arial,sans-serif;color:var(--text-dark)}
.screen{position:absolute;overflow:hidden;background:linear-gradient(180deg,var(--paper-hi),var(--paper-lo))}
.screen--home{left:20px;top:9px;width:570px;height:431px}
.screen--news{left:618px;top:18px;width:560px;height:422px}
.screen--brands{left:20px;top:459px;width:561px;height:421px}
.screen--about{left:609px;top:459px;width:569px;height:421px}
.abs{position:absolute}
.nav{position:absolute;left:0;top:0;right:0;background:var(--ink)}
.nav__mark{position:absolute;background:var(--red)}
.nav__name{position:absolute;color:var(--white);font-weight:700;font-size:13px;white-space:nowrap}
.nav__item{position:absolute;color:var(--nav-text);font-size:9px;text-transform:uppercase;letter-spacing:.2px;white-space:nowrap}
.nav__item--active{color:var(--white)}
.nav__divider{position:absolute;top:0;bottom:0;width:1px;background:var(--divider)}
.section-title{position:absolute;font-weight:700;font-size:14px;color:var(--text-dark);text-transform:uppercase;letter-spacing:.2px;white-space:nowrap}
.section-marker{position:absolute;width:11px;height:24px;background:var(--red)}
.section-marker svg{display:block}
.rule{position:absolute;height:1px;background:var(--rule)}
.see-more{position:absolute;background:var(--button);color:#cfcfcf;font-size:9px;text-align:center}
.photo{position:absolute}
.label-red{position:absolute;color:var(--red);font-weight:700;font-size:12px;white-space:nowrap}
.label-title{position:absolute;color:var(--white);font-weight:700;font-size:10px;white-space:nowrap}
.news-date{position:absolute;color:var(--red);font-size:9px}
.news-title{position:absolute;color:var(--white);font-weight:700;font-size:10px;white-space:nowrap}
.small{position:absolute;font-size:8px;line-height:11px;color:var(--text-mid)}
.small--light{color:#bbb;white-space:nowrap}
</style>
</head>
<body>

<!-- Home -->
<section class="screen screen--home">
  <nav class="nav" style="height:69px">
    <span class="nav__mark" style="left:0;top:10px;width:22px;height:45px"></span>
    <span class="nav__name" style="left:32px;top:25px">Cosmetics Store</span>
    <span class="nav__item nav__item--active" style="left:197px;top:28px">Home</span>
    <span class="nav__divider" style="left:254px;top:12px"></span>
    <span class="nav__item" style="left:291px;top:28px">About</span>
    <span class="nav__divider" style="left:352px;top:12px"></span>
    <span class="nav__item" style="left:378px;top:28px">Locations</span>
    <span class="nav__divider" style="left:448px;top:12px"></span>
    <span class="nav__item" style="left:488px;top:28px">Brands</span>
  </nav>

  <span class="section-marker" style="left:0;top:110px"><svg width="11" height="24"><path d="M3 7l5 5-5 5" fill="none" stroke="#fff" stroke-width="1.5"/></svg></span>
  <h2 class="section-title" style="left:16px;top:115px">This Season</h2>

  <div class="abs" style="left:0;top:149px;width:130px;height:276px;background:#8f8f8f"></div>
  <div class="abs" style="left:0;top:163px;width:118px;height:202px;background:var(--white)">
    <span class="abs" style="left:8px;top:6px;font-size:12px;color:var(--text-dark);white-space:nowrap"><b>skin</b> care guide</span>
    <div class="photo" role="img" aria-label="Featured skincare campaign photo" style="left:0;top:22px;width:118px;height:180px;background:linear-gradient(180deg,#f2f2f2 0%,#e8d5cc 40%,#c8231d 70%,#b51712 100%)"></div>
  </div>
  <span class="label-red" style="left:0;top:375px;font-size:11px">Featured</span>
  <span class="label-title" style="left:0;top:393px">Our spring skin edit.</span>

  <div class="abs" style="left:142px;top:108px;width:420px;height:317px;background:var(--ink)"></div>
  <div class="photo" role="img" aria-label="Video still: tour of the store's beauty counters" style="left:142px;top:121px;width:420px;height:304px;background:linear-gradient(100deg,#2a2420 0%,#5b4a40 30%,#c9a58f 48%,#d4688a 68%,#b8123a 85%,#e04060 100%)"></div>
  <span class="abs" style="left:150px;top:150px;color:var(--white);font-size:18px">lumen tv</span>
  <svg class="abs" style="left:330px;top:252px" width="44" height="44" viewBox="0 0 44 44"><rect width="44" height="44" rx="6" fill="#000" fill-opacity=".8"/><path d="M17 13l14 9-14 9z" fill="#fff"/></svg>
</section>

<!-- News and locations -->
<section class="screen screen--news">
  <span class="section-marker" style="left:9px;top:32px"><svg width="11" height="24"><path d="M3 7l5 5-5 5" fill="none" stroke="#fff" stroke-width="1.5"/></svg></span>
  <h2 class="section-title" style="left:27px;top:37px">Store News</h2>
  <span class="see-more" style="left:493px;top:34px;width:41px;height:18px;line-height:18px">see more</span>
  <div class="rule" style="left:9px;right:20px;top:64px"></div>

  <div class="photo" role="img" aria-label="News photo: new skincare line on display" style="left:11px;top:70px;width:124px;height:111px;background:linear-gradient(180deg,#c9cdd3,#7b7f86 60%,#1a1a1a)"></div>
  <div class="photo" role="img" aria-label="News photo: facial treatment room" style="left:144px;top:70px;width:124px;height:111px;background:linear-gradient(180deg,#8f8a84,#c5beb6 40%,#b8201c 80%)"></div>
  <div class="photo" role="img" aria-label="News photo: makeup artist at work" style="left:278px;top:70px;width:124px;height:111px;background:linear-gradient(180deg,#a9b5c4,#7d8896 50%,#1c1c1c)"></div>
  <div class="photo" role="img" aria-label="News photo: store team welcoming guests" style="left:411px;top:70px;width:124px;height:111px;background:linear-gradient(180deg,#8a9bb0,#b8a295 50%,#e4d6cc)"></div>

  <span class="news-date" style="left:11px;top:194px">07/18/2023</span>
  <span class="news-date" style="left:144px;top:194px">07/18/2023</span>
  <span class="news-date" style="left:278px;top:194px">07/18/2023</span>
  <span class="news-date" style="left:411px;top:194px">07/18/2023</span>
  <span class="news-title" style="left:11px;top:209px">New skincare lines</span>
  <span class="news-title" style="left:144px;top:209px">Facial bar now open</span>
  <span class="news-title" style="left:278px;top:209px">Meet our artists</span>
  <span class="news-title" style="left:411px;top:209px">We are hiring</span>
  <p class="small" style="left:11px;top:229px;width:122px">Three luxury skincare lines arrive in all our stores this month. Ask our advisors for a free skin consultation.</p>
  <p class="small" style="left:144px;top:229px;width:122px">Book a relaxing facial with our licensed estheticians. Treatments use the lines we carry in store.</p>
  <p class="small" style="left:278px;top:229px;width:122px">Our makeup artists offer lessons, bridal looks and event makeup. Walk in or book ahead online.</p>
  <p class="small" style="left:411px;top:229px;width:122px">Join a locally owned team. We are looking for beauty advisors and estheticians at every store.</p>
  <div class="rule" style="left:9px;right:20px;top:322px"></div>

  <span class="section-marker" style="left:9px;top:335px"><svg width="11" height="24"><path d="M3 7l5 5-5 5" fill="none" stroke="#fff" stroke-width="1.5"/></svg></span>
  <h2 class="section-title" style="left:27px;top:340px">Our Locations</h2>
  <span class="see-more" style="left:493px;top:338px;width:41px;height:18px;line-height:18px">see more</span>

  <div class="abs" style="left:0;top:374px;width:545px;height:48px;background:var(--strip)"></div>
  <div class="nav__divider" style="left:134px;top:374px;bottom:0"></div>
  <div class="nav__divider" style="left:268px;top:374px;bottom:0"></div>
  <div class="nav__divider" style="left:402px;top:374px;bottom:0"></div>
  <span class="label-red" style="left:11px;top:390px">Boise</span>
  <span class="label-red" style="left:144px;top:390px">Meridian</span>
  <span class="label-red" style="left:278px;top:390px">Nampa</span>
  <span class="label-red" style="left:411px;top:390px">Eagle</span>
  <span class="label-title" style="left:11px;top:406px">Downtown flagship</span>
  <span class="label-title" style="left:144px;top:406px">The Village shops</span>
  <span class="label-title" style="left:278px;top:406px">Main Street store</span>
  <span class="label-title" style="left:411px;top:406px">State Street store</span>
</section>

<!-- Brands -->
<section class="screen screen--brands">
  <nav class="nav" style="height:62px">
    <span class="nav__mark" style="left:10px;top:4px;width:24px;height:49px"></span>
    <span class="nav__name" style="left:42px;top:22px;font-size:12px">Cosmetics Store</span>
    <span class="nav__item" style="left:211px;top:24px">Home</span>
    <span class="nav__divider" style="left:256px"></span>
    <span class="nav__item" style="left:302px;top:24px">About</span>
    <span class="nav__divider" style="left:349px"></span>
    <span class="nav__item" style="left:374px;top:24px">Locations</span>
    <span class="nav__divider" style="left:440px"></span>
    <span class="nav__item nav__item--active" style="left:477px;top:24px">Brands</span>
  </nav>
  <span class="abs" style="left:475px;top:66px;width:74px;height:18px;background:#bdbdbd;color:#7a7a7a;font-size:8px;line-height:18px;text-align:center">ALL BRANDS</span>

  <span class="section-marker" style="left:10px;top:106px"><svg width="11" height="24"><path d="M3 7l5 5-5 5" fill="none" stroke="#fff" stroke-width="1.5"/></svg></span>
  <h2 class="section-title" style="left:28px;top:111px">Our Brands</h2>
  <div class="rule" style="left:10px;right:20px;top:141px"></div>

  <div class="photo" role="img" aria-label="Skincare products photo" style="left:22px;top:164px;width:121px;height:199px;background:linear-gradient(180deg,#5d87b8 0%,#8c8c88 30%,#6f6a64 60%,#b51c18 80%,#4a4540)"></div>
  <div class="photo" role="img" aria-label="Makeup products photo" style="left:154px;top:164px;width:120px;height:199px;background:linear-gradient(180deg,#a8adb5 0%,#c8ccd2 30%,#1c1c1c 50%,#c82a22 65%,#8a7a5c 100%)"></div>
  <div class="photo" role="img" aria-label="Fragrance bottles photo" style="left:286px;top:164px;width:119px;height:199px;background:linear-gradient(180deg,#f4f4f4 0%,#e0cfc6 30%,#c8231d 55%,#a8a8a8 100%)"></div>
  <div class="photo" role="img" aria-label="Body care products photo" style="left:418px;top:164px;width:119px;height:199px;background:linear-gradient(180deg,#6b7a8e 0%,#a2acb8 35%,#2a2a2a 70%,#3e3a36 100%)"></div>

  <div class="abs" style="left:22px;top:363px;width:515px;height:43px;background:var(--strip)"></div>
  <span class="label-red" style="left:25px;top:374px;font-size:11px">Skincare</span>
  <span class="label-red" style="left:157px;top:374px;font-size:11px">Makeup</span>
  <span class="label-red" style="left:289px;top:374px;font-size:11px">Fragrance</span>
  <span class="label-red" style="left:421px;top:374px;font-size:11px">Body Care</span>
  <span class="small small--light" style="left:25px;top:391px">Serums, creams, masks</span>
  <span class="small small--light" style="left:157px;top:391px">Color, brushes, primers</span>
  <span class="small small--light" style="left:289px;top:391px">Perfumes and colognes</span>
  <span class="small small--light" style="left:421px;top:391px">Lotions, oils, scrubs</span>
</section>

<!-- About -->
<section class="screen screen--about">
  <nav class="nav" style="height:62px;width:558px">
    <span class="nav__mark" style="left:8px;top:4px;width:22px;height:49px"></span>
    <span class="nav__name" style="left:39px;top:22px;font-size:12px">Cosmetics Store</span>
    <span class="nav__item" style="left:207px;top:24px">Home</span>
    <span class="nav__divider" style="left:252px"></span>
    <span class="nav__item nav__item--active" style="left:299px;top:24px">About</span>
    <span class="nav__divider" style="left:346px"></span>
    <span class="nav__item" style="left:370px;top:24px">Locations</span>
    <span class="nav__divider" style="left:437px"></span>
    <span class="nav__item" style="left:495px;top:24px">Brands</span>
  </nav>

  <span class="section-marker" style="left:8px;top:107px"><svg width="11" height="24"><path d="M3 7l5 5-5 5" fill="none" stroke="#fff" stroke-width="1.5"/></svg></span>
  <h2 class="section-title" style="left:25px;top:112px">About Us</h2>
  <div class="rule" style="left:8px;right:20px;top:142px"></div>

  <div class="photo" role="img" aria-label="Photo of the flagship store interior" style="left:19px;top:173px;width:183px;height:248px;background:linear-gradient(180deg,#5a86bd 0%,#7d7c78 25%,#5c5853 50%,#c01e19 75%,#3a3633 100%)"></div>

  <h3 class="abs" style="left:217px;top:178px;font-size:19px;font-weight:400;color:var(--text-dark);white-space:nowrap">Our mission.</h3>
  <p class="abs" style="left:217px;top:212px;width:330px;font-size:10.5px;line-height:14px;font-weight:700;color:var(--highlight)">We are a locally owned Idaho store bringing high end cosmetics and skincare to our community, with expert advice and personal service at every counter.</p>
  <p class="small" style="left:217px;top:278px;width:330px">Our beauty advisors help you find the right products for your skin. We offer facials, makeup lessons and event makeup in each of our stores, and we do not sell online, so every visit is personal.</p>
  <p class="small" style="left:217px;top:334px;width:330px">We carry a curated list of luxury skincare, makeup, fragrance and body care lines. Visit one of our four locations across the Treasure Valley, or read about careers with our team. We are always glad to meet people who love beauty as much as we do.</p>
</section>

</body>
</html>
```